Paint Protection Options

This is a flyer that will describe two different paint protection options for vehicles. I have mocked up a Word doc. As well, I've included some samples of other flyers where I like the "look". I am not locked into any single layout or design. In my Word doc I have them side-by-side. I think that makes sense but open to ideas. I've also added some pics of the two options being applied to cars. We need to have one of each (ceramic and ppf) at a minimum. In the grid I'm thinking different colors dots/circles to differentiate the different levels. But again, I'm open to suggestions. You can use the symbol for microns in the grid under the Thickness row. I spelled it out because I didn't know how to insert.

```html
<!DOCTYPE html>
<html lang="en">
<head>
<meta charset="utf-8">
<title>Paint Protection Options</title>
<link href="https://fonts.googleapis.com/css2?family=Poppins:wght@400;500;600;700;800&display=swap" rel="stylesheet">
<style>
  :root{
    --stage:#7b8590;
    --navy:#1e3050;
    --navy-deep:#17253f;
    --sky:#1fa9e1;
    --card-bg:#eaf7fd;
    --card-line:#29abe2;
    --ink:#1a1a1a;
    --row-light:#e6edf8;
    --row-dark:#c2d3ea;
    --row-light-alt:#d9e3f1;
    --row-dark-alt:#b3c7e2;
    --head-grey:#474747;
    --head-wax:#dc0aa0;
    --head-ceramic:#0d1d96;
    --head-ppf:#e8161c;
    --dot-low:#f7d117;
    --dot-mid:#0c9a2c;
    --dot-high:#ee1010;
    --accent-cyan:#22d3f0;
  }
  *{box-sizing:border-box;margin:0;padding:0}
  html,body{width:1027px;height:1200px;overflow:hidden}
  body{background:var(--stage);font-family:"Poppins",sans-serif;color:var(--ink)}
  .flyer{position:absolute;left:50px;top:0;width:927px;height:1200px;background:#fff;overflow:hidden}

  .hero{position:absolute;left:0;top:0;width:927px;height:334px;background:var(--navy)}
  .hero-photo{position:absolute;left:500px;top:0;width:427px;height:334px;
    background:
      radial-gradient(ellipse 70% 55% at 85% 95%, #e0140f 0%, #b80d0d 35%, rgba(120,10,15,0) 70%),
      radial-gradient(ellipse 40% 45% at 50% 35%, #3c4656 0%, rgba(40,48,62,0) 70%),
      linear-gradient(90deg, var(--navy) 0%, #1c2433 30%, #151a23 100%)}
  .hero-title{position:absolute;left:62px;top:82px;font-weight:800;font-size:70px;line-height:65px;letter-spacing:-2.5px;color:#fff}
  .hero-title .accent{color:var(--sky)}

  .card{position:absolute;top:328px;width:398px;height:411px;background:var(--card-bg);border:1px solid var(--card-line);border-radius:4px 4px 30px 30px}
  .card-ceramic{left:62px}
  .card-ppf{left:476px}
  .card h2{position:absolute;left:12px;top:22px;font-weight:800;font-size:27px;line-height:29px;letter-spacing:-0.5px;color:var(--navy)}
  .card h2 .accent{color:var(--sky)}
  .card p{position:absolute;left:16px;width:366px;font-size:11.4px;line-height:14.3px;color:#222}
  .card .rule{position:absolute;left:12px;right:14px;border-top:1px dashed #8a8a8a}
  .card ul{position:absolute;left:16px;list-style:none;font-size:12.6px;line-height:15px;font-weight:500;color:#111}
  .card li{position:relative;padding-left:20px;margin-bottom:7px}
  .card li svg{position:absolute;left:0;top:3px;width:10px;height:10px}
  .card-ppf ul li{margin-bottom:3px}

  .compare{position:absolute;left:62px;top:768px;width:806px}
  .col{position:absolute;top:0;width:196px}
  .col-head{height:37px;display:flex;align-items:center;justify-content:center;color:#fff;font-weight:700;font-size:13px;letter-spacing:0.2px}
  .col-body{margin-top:7px}
  .cell{height:24.4px;display:flex;align-items:center;justify-content:center;font-size:10.5px;color:#1b1b1b}
  .cell:nth-child(odd){background:var(--row-light)}
  .cell:nth-child(even){background:var(--row-dark)}
  .col-ceramic .cell:nth-child(odd){background:var(--row-light-alt)}
  .col-ceramic .cell:nth-child(even){background:var(--row-dark-alt)}
  .cell.gauge{height:33px}
  .cell svg.dot{width:10px;height:10px}
  .cell svg.meter{width:34px;height:18px}

  .col-feature{left:0}
  .col-feature .col-head{background:var(--head-grey)}
  .col-feature .col-body{background:var(--navy)}
  .col-feature .cell{justify-content:flex-start;padding-left:14px;color:#fff;background:var(--navy)!important}
  .col-feature .cell:nth-child(even){background:var(--navy-deep)!important}
  .col-feature .cell.gauge{color:var(--accent-cyan);font-weight:600;font-size:10.5px}
  .col-wax{left:204px;width:195px}
  .col-wax .col-head{background:var(--head-wax)}
  .col-ceramic{left:407px}
  .col-ceramic .col-head{background:var(--head-ceramic)}
  .col-ppf{left:610px}
  .col-ppf .col-head{background:var(--head-ppf)}

  .legend{position:absolute;left:62px;top:1131px;display:flex;gap:0;font-weight:700;font-size:13px;color:#111}
  .legend span{display:flex;align-items:center;gap:6px}
  .legend i{display:block;width:13px;height:13px;border-radius:50%}
  .legend .low{width:82px}.legend .low i{background:var(--dot-low)}
  .legend .mid{width:101px}.legend .mid i{background:var(--dot-mid)}
  .legend .high i{background:var(--dot-high)}

  .visit{position:absolute;left:378px;top:1124px;width:490px;height:32px;border-radius:16px;background:var(--row-dark);overflow:hidden}
  .visit-label{position:absolute;left:22px;top:0;line-height:32px;font-size:13px;letter-spacing:2.4px;color:#22304c}
  .visit-url{position:absolute;left:138px;top:0;right:0;height:32px;border-radius:16px;background:var(--navy);color:#fff;font-size:12.5px;letter-spacing:3px;line-height:32px;text-align:center}
</style>
</head>
<body>
<svg width="0" height="0" style="position:absolute">
  <defs>
    <symbol id="dot-green" viewBox="0 0 10 10"><circle cx="5" cy="5" r="5" fill="#0c9a2c"/></symbol>
    <symbol id="dot-red" viewBox="0 0 10 10"><circle cx="5" cy="5" r="5" fill="#ee1010"/></symbol>
    <symbol id="dot-yellow-half" viewBox="0 0 10 10"><circle cx="5" cy="5" r="4.6" fill="#fff" stroke="#f7d117" stroke-width="0.8"/><path d="M5 0 A5 5 0 0 1 5 10 Z" fill="#f7d117"/></symbol>
    <symbol id="dot-yellow-quarter" viewBox="0 0 10 10"><circle cx="5" cy="5" r="4.6" fill="#fff" stroke="#f7d117" stroke-width="0.8"/><path d="M5 5 L5 0 A5 5 0 0 1 10 5 Z" fill="#f7d117"/></symbol>
    <symbol id="dot-green-part" viewBox="0 0 10 10"><circle cx="5" cy="5" r="4.6" fill="#fff" stroke="#0c9a2c" stroke-width="0.8"/><path d="M5 5 L5 0 A5 5 0 1 1 0 5 Z" fill="#0c9a2c"/></symbol>
    <symbol id="tick" viewBox="0 0 10 10"><circle cx="5" cy="5" r="5" fill="#1fa9e1"/><path d="M2.8 5.2 L4.4 6.7 L7.3 3.6" fill="none" stroke="#fff" stroke-width="1.3"/></symbol>
    <symbol id="meter-arc" viewBox="0 0 34 18">
      <path d="M4 16 A13 13 0 0 1 9 6" fill="none" stroke="#0c9a2c" stroke-width="3"/>
      <path d="M10 5.3 A13 13 0 0 1 17 3" fill="none" stroke="#f7d117" stroke-width="3"/>
      <path d="M18 3 A13 13 0 0 1 30 16" fill="none" stroke="#ee1010" stroke-width="3"/>
    </symbol>
  </defs>
</svg>

<main class="flyer">
  <header class="hero">
    <div class="hero-photo" role="img" aria-label="Photo of a detailer in a mask polishing the bonnet of a red car with a machine polisher"></div>
    <h1 class="hero-title">PAINT<br>PROTECTION<br><span class="accent">OPTIONS</span></h1>
  </header>

  <section class="card card-ceramic">
    <h2><span class="accent">CERAMIC</span> COATINGS</h2>
    <p style="top:70px">Ceramic coatings are liquid polymer coatings that bond to a vehicle’s painted surface. The coatings are formulated to retain the showroom finish by protecting against corrosion and contaminants like UV damage, oxidation, road salt and acid rain.&nbsp; Ceramic coatings give your car a deep, glossy finish that reflects light and makes your paint look more vibrant while greatly extending the paint's lifespan.</p>
    <div class="rule" style="top:186px"></div>
    <p style="top:215px">The chemical bonding process improves color depth and leaves a smooth finish. The hydrophobic (water repellent) properties repel water and dirt as well as protect against damaging pollutants.&nbsp; This makes care and maintenance a breeze while retaining the show room finish.<br>Never wax again!</p>
    <ul style="top:313px">
      <li><svg><use href="#tick"/></svg>Enhance and retain showroom finish</li>
      <li><svg><use href="#tick"/></svg>Protect against corrosion and contaminants</li>
      <li><svg><use href="#tick"/></svg>Reduce care and maintenance</li>
    </ul>
  </section>

  <section class="card card-ppf">
    <h2><span class="accent">PAINT PROTECTION</span><br>FILM (PPF)</h2>
    <p style="top:99px">Paint Protection Film (PPF) is a transparent, thermoplastic urethane film that is applied directly to the car’s painted surfaces. PPF excels at shielding your vehicle from rock chips, scratches, and other physical damage. It has self-healing properties that can repair minor scratches and swirl marks over time.</p>
    <div class="rule" style="top:197px"></div>
    <p style="top:207px">Paint Protection Film (PPF) is a transparent, thermoplastic urethane film that is applied directly to the car’s painted surfaces. PPF excels at shielding your vehicle from rock chips, scratches, and other physical damage. It has self-healing properties that can repair minor scratches and swirl marks over time.</p>
    <ul style="top:306px">
      <li><svg><use href="#tick"/></svg>Protect against rock chips, scratches,<br>and physical damage</li>
      <li><svg><use href="#tick"/></svg>Easily repair minor scratches and swirl marks</li>
      <li><svg><use href="#tick"/></svg>Protect against corrosion and contaminants</li>
    </ul>
  </section>

  <section class="compare">
    <div class="col col-feature">
      <div class="col-head">FEATURE</div>
      <div class="col-body">
        <div class="cell">Duration</div>
        <div class="cell">Thickness</div>
        <div class="cell">Gloss Enhancement</div>
        <div class="cell">Acid Rain Damage</div>
        <div class="cell">Corrosion Prevention</div>
        <div class="cell">UV/Oxidation Protection</div>
        <div class="cell">Hard Water Damage</div>
        <div class="cell">Insect Splatter Damage</div>
        <div class="cell">Chip Protection</div>
        <div class="cell">Scratch Protection</div>
        <div class="cell">Swirl Protection</div>
        <div class="cell gauge">Application Complexity</div>
      </div>
    </div>

    <div class="col col-wax">
      <div class="col-head">CAR WAX</div>
      <div class="col-body">
        <div class="cell">2 - 4 Weeks</div>
        <div class="cell">.5 - 1.5 µm</div>
        <div class="cell"><svg class="dot"><use href="#dot-green"/></svg></div>
        <div class="cell"><svg class="dot"><use href="#dot-yellow-half"/></svg></div>
        <div class="cell"><svg class="dot"><use href="#dot-yellow-half"/></svg></div>
        <div class="cell"><svg class="dot"><use href="#dot-yellow-half"/></svg></div>
        <div class="cell"><svg class="dot"><use href="#dot-yellow-quarter"/></svg></div>
        <div class="cell"><svg class="dot"><use href="#dot-yellow-quarter"/></svg></div>
        <div class="cell"><svg class="dot"><use href="#dot-red"/></svg></div>
        <div class="cell"><svg class="dot"><use href="#dot-red"/></svg></div>
        <div class="cell"><svg class="dot"><use href="#dot-red"/></svg></div>
        <div class="cell gauge"><svg class="meter" viewBox="0 0 34 18"><use href="#meter-arc"/><path d="M17 16 L6 11" stroke="#111" stroke-width="2"/></svg></div>
      </div>
    </div>

    <div class="col col-ceramic">
      <div class="col-head">CERAMIC COATING</div>
      <div class="col-body">
        <div class="cell">3 - 10 Years</div>
        <div class="cell">7 - 10 µm</div>
        <div class="cell"><svg class="dot"><use href="#dot-green"/></svg></div>
        <div class="cell"><svg class="dot"><use href="#dot-green"/></svg></div>
        <div class="cell"><svg class="dot"><use href="#dot-green"/></svg></div>
        <div class="cell"><svg class="dot"><use href="#dot-green"/></svg></div>
        <div class="cell"><svg class="dot"><use href="#dot-green-part"/></svg></div>
        <div class="cell"><svg class="dot"><use href="#dot-green-part"/></svg></div>
        <div class="cell"><svg class="dot"><use href="#dot-yellow-quarter"/></svg></div>
        <div class="cell"><svg class="dot"><use href="#dot-yellow-quarter"/></svg></div>
        <div class="cell"><svg class="dot"><use href="#dot-red"/></svg></div>
        <div class="cell gauge"><svg class="meter" viewBox="0 0 34 18"><use href="#meter-arc"/><path d="M17 17 L15 6" stroke="#111" stroke-width="2"/></svg></div>
      </div>
    </div>

    <div class="col col-ppf">
      <div class="col-head">PAINT PROTECTION FILM</div>
      <div class="col-body">
        <div class="cell">7 - 10 Years</div>
        <div class="cell">200 - 250 µm</div>
        <div class="cell"><svg class="dot"><use href="#dot-green"/></svg></div>
        <div class="cell"><svg class="dot"><use href="#dot-green"/></svg></div>
        <div class="cell"><svg class="dot"><use href="#dot-green"/></svg></div>
        <div class="cell"><svg class="dot"><use href="#dot-green"/></svg></div>
        <div class="cell"><svg class="dot"><use href="#dot-green"/></svg></div>
        <div class="cell"><svg class="dot"><use href="#dot-green"/></svg></div>
        <div class="cell"><svg class="dot"><use href="#dot-green"/></svg></div>
        <div class="cell"><svg class="dot"><use href="#dot-green"/></svg></div>
        <div class="cell"><svg class="dot"><use href="#dot-green"/></svg></div>
        <div class="cell gauge"><svg class="meter" viewBox="0 0 34 18"><use href="#meter-arc"/><path d="M15 17 L24 7" stroke="#111" stroke-width="2"/></svg></div>
      </div>
    </div>
  </section>

  <footer>
    <div class="legend">
      <span class="low"><i></i>LOW</span>
      <span class="mid"><i></i>MEDIUM</span>
      <span class="high"><i></i>HIGH</span>
    </div>
    <div class="visit">
      <span class="visit-label">VISIT US AT</span>
      <span class="visit-url">www.glossguardstudio.com</span>
    </div>
  </footer>
</main>
</body>
</html>
```